Graphic Design Vendora Book Description

There is a book on Vendora that is my competitor that has a large graphic design as part of the description for the book and I want a similar thing for my book to make it stand out more.

My competitors book is here: https://www.vendora-shop.example/Tidal-Lore-Starters-Grasping-Overview/dp/K31RTWP704/

My book is here: https://www.vendora-shop.example/Tidal-Lore-Groundwork-Workings-Interlacing/dp/K7Q2FXH58C/

You can see the kind of thing I am looking for on the book listing but I have attached an image below.

Thanks

Colin

```html
<!DOCTYPE html>
<html lang="en">
<head>
<meta charset="utf-8">
<title>Vendora Book Listing – Quantum Physics</title>
<link rel="stylesheet" href="https://fonts.googleapis.com/css2?family=Bebas+Neue&family=Arimo:wght@400;700&display=swap">
<style>
:root{
  --yellow:#f5e63a;
  --yellow-deep:#e3c413;
  --black:#050505;
  --space:#1c1d22;
  --text:#0f1111;
  --muted:#565959;
  --link:#007185;
  --star:#de7921;
  --price:#0f1111;
  --rule:#e3e6e6;
  --white:#ffffff;
}
*{box-sizing:border-box;margin:0;padding:0}
html,body{width:1200px;height:3322px;overflow:hidden;background:var(--white)}
body{position:relative;font-family:"Arimo",Arial,sans-serif;color:var(--text)}

/* carousel */
.carousel-head{position:absolute;top:26px;left:0;width:1200px;border-top:1px solid var(--rule);padding-top:12px;font-size:15px}
.carousel-head .page{position:absolute;right:14px;top:14px;font-size:12px}
.carousel-arrow{position:absolute;top:171px;width:28px;height:34px;border:1px solid #bbb;border-radius:6px;background:#fff;box-shadow:0 1px 3px rgba(0,0,0,.15)}
.carousel-arrow svg{position:absolute;left:8px;top:11px}
.carousel-arrow.prev{left:6px}
.carousel-arrow.next{left:1151px}
.item{position:absolute;top:65px;width:144px;font-size:11px;line-height:15px}
.item .cover{display:block;height:134px;width:84px;margin-left:25px;margin-bottom:8px}
.item .title{color:var(--link);display:block;font-size:11.5px;line-height:16px}
.item .author{color:var(--muted);font-size:10px}
.item .rating{color:var(--star);font-size:12px;letter-spacing:-1px}
.item .rating span{color:var(--link);font-size:10px;letter-spacing:0;margin-left:4px}
.item .format{color:var(--muted);font-size:10px}
.item .price{font-size:14px;color:var(--price)}
.item .price sup{font-size:9px}
.item .ship{color:var(--muted);font-size:10px}

/* banners */
.banner{position:absolute;left:164px;width:875px;overflow:hidden;
  background:radial-gradient(ellipse at 70% 40%,#3b3d45 0%,#1a1b20 45%,#050505 100%)}
.banner .headline{position:absolute;left:48px;font-family:"Bebas Neue",Impact,sans-serif;color:var(--white);font-size:76px;line-height:72px}
.hl{color:var(--yellow)}
.mockup{position:absolute;background:linear-gradient(135deg,var(--yellow) 0%,var(--yellow-deep) 100%)}

.hero{top:423px;height:541px;background:linear-gradient(90deg,#000 0%,#0c0c0c 55%,#222 100%)}
.hero .headline{left:63px;top:56px;font-size:68px;line-height:66px}
.hero .topics{position:absolute;left:63px;top:238px;list-style:none;font-family:"Bebas Neue",Impact,sans-serif;font-size:36px;line-height:53px;color:var(--white)}
.hero .topics b{color:var(--yellow);font-weight:400;margin-right:14px}
.hero .byline{position:absolute;left:66px;top:478px;font-family:"Bebas Neue",Impact,sans-serif;font-size:20px;color:var(--yellow)}
.hero .byline span{color:var(--white)}

/* feature tiles */
.tile{position:absolute;top:974px;width:212px;height:210px;overflow:hidden;font-family:"Bebas Neue",Impact,sans-serif}
.tile.bright{background:radial-gradient(circle at 55% 30%,#fff7a8 0%,var(--yellow) 35%,#d9a90c 100%);color:#111}
.tile.dark{background:radial-gradient(circle at 50% 45%,#4a4c55 0%,#1d1e24 60%,#08080a 100%);color:var(--white)}
.tile .num{position:absolute;right:18px;top:14px;font-size:66px;line-height:66px}
.tile.dark .num{color:var(--yellow)}
.tile .label{position:absolute;left:20px;bottom:38px;font-size:32px;line-height:32px}
.tile .icon{position:absolute;left:22px;top:22px}
.tile-copy{position:absolute;top:1204px;width:190px;font-size:12.5px;line-height:16px;color:#222}

.journey{top:1335px;height:542px}
.journey .headline{top:60px}
.secrets{top:1885px;height:541px}
.secrets .headline{top:44px}
.power{top:2436px;height:547px;left:160px;width:881px}
.power .headline{top:58px}

/* product details */
.details-rule{position:absolute;left:50px;width:1150px;border-top:1px solid var(--rule)}
.details-title{position:absolute;left:50px;top:3058px;font-size:24px;font-weight:400}
.details{position:absolute;left:67px;top:3098px;list-style:none;font-size:13px;line-height:24px}
.details b{font-weight:700}
.details a{color:var(--link);text-decoration:none}
.details .stars{color:var(--star);font-size:15px;letter-spacing:-1px}
</style>
</head>
<body>

<header class="carousel-head">More items to explore<span class="page">Page 1 of 7</span></header>
<div class="carousel-arrow prev"><svg width="10" height="12" viewBox="0 0 10 12"><path d="M7 1L2 6l5 5" fill="none" stroke="#333" stroke-width="2"/></svg></div>
<div class="carousel-arrow next"><svg width="10" height="12" viewBox="0 0 10 12"><path d="M3 1l5 5-5 5" fill="none" stroke="#333" stroke-width="2"/></svg></div>

<div class="item" style="left:58px">
  <span class="cover" role="img" aria-label="Book cover, dark starfield" style="background:linear-gradient(#1b2440,#3a2a22)"></span>
  <span class="title">Starlight for Busy Readers: Essays on the Universe and Our Place Within It</span>
  <div class="author">Orin Castellane</div>
  <div class="rating">★★★★★<span>34,928</span></div>
  <div class="format">Hardcover</div>
  <div class="price"><sup>£</sup>12.99</div>
  <div class="ship">£2.74 delivery</div>
</div>
<div class="item" style="left:215px">
  <span class="cover" role="img" aria-label="Book cover, green nebula" style="background:linear-gradient(#1e3b1a,#5b7a2a)"></span>
  <span class="title">Hidden Mass &amp; Silent Energy: The Unseen 95% of the Universe (Hot…</span>
  <div class="author">› Rowan Tillet</div>
  <div class="rating">★★★★★<span>1,166</span></div>
  <div class="format">Paperback</div>
  <div class="price"><sup>£</sup>8.49</div>
  <div class="ship" style="color:#0f1111">Get it as soon as <b>Friday, Aug 16</b></div>
  <div class="ship">£2.68 delivery</div>
</div>
<div class="item" style="left:373px">
  <span class="cover" role="img" aria-label="Book cover, pale with line drawing" style="background:linear-gradient(#f4f3ee,#e2e0d6)"></span>
  <span class="title">Classical Motion: The Essential Minimum</span>
  <div class="author">Petra Dolvenko</div>
  <div class="rating">★★★★★<span>946</span></div>
  <div class="format">Paperback</div>
  <div class="price"><sup>£</sup>9.65</div>
  <div class="ship">£2.68 delivery</div>
</div>
<div class="item" style="left:530px">
  <span class="cover" role="img" aria-label="Book cover, dark red with gold type" style="background:linear-gradient(#3d1b14,#7a3a1c)"></span>
  <span class="title">The Grand Equation: The Origin and Fate of the Universe</span>
  <div class="author">› Julian Marsh</div>
  <div class="rating">★★★★★<span>14,845</span></div>
  <div class="format">Paperback</div>
  <div class="price"><sup>£</sup>11.99</div>
  <div class="ship">£2.66 delivery</div>
</div>
<div class="item" style="left:686px">
  <span class="cover" role="img" aria-label="Book cover, black with glowing ring" style="background:radial-gradient(circle,#5a3b8a,#050505 70%)"></span>
  <span class="title">Dark Wells: The Key to Understanding the Universe</span>
  <div class="author">Professor Evan Rook</div>
  <div class="rating">★★★★★<span>798</span></div>
  <div class="format">Paperback</div>
  <div class="price"><sup>£</sup>9.93</div>
  <div class="ship">£2.77 delivery</div>
</div>
<div class="item" style="left:844px">
  <span class="cover" role="img" aria-label="Book cover, pale with line drawing" style="background:linear-gradient(#f4f3ee,#e2e0d6)"></span>
  <span class="title">Quantum Motion: The Essential Minimum</span>
  <div class="author">› Lionel Saxby</div>
  <div class="rating">★★★★★<span>2,184</span></div>
  <div class="format">Paperback</div>
  <div class="price"><sup>£</sup>10.11</div>
  <div class="ship">£2.77 delivery</div>
</div>
<div class="item" style="left:1000px">
  <span class="cover" role="img" aria-label="Book cover, white with black cat silhouette" style="background:linear-gradient(#ffffff,#d8d8d8)"></span>
  <span class="title">Chasing the Boxed Cat: The bestselling classic introduction to quantu…</span>
  <div class="author">Jonah Grell</div>
  <div class="rating">★★★★★<span>1,001</span></div>
  <div class="format">Paperback</div>
  <div class="price"><sup>£</sup>9.85</div>
  <div class="ship">£2.77 delivery</div>
</div>

<section class="banner hero">
  <h1 class="headline">A <span class="hl">Beginners<br>Guide to...</span></h1>
  <ol class="topics">
    <li><b>01</b>Quantum Mechanics,</li>
    <li><b>02</b>String Theory,</li>
    <li><b>03</b>Field Theory, and</li>
    <li><b>04</b>Quantum Computing</li>
  </ol>
  <p class="byline">Written by: <span>Elias Thorne</span></p>
  <div class="mockup" role="img" aria-label="Yellow Quantum Physics book, front and back cover, over a chalkboard of equations" style="left:420px;top:50px;width:410px;height:440px"></div>
</section>

<div class="tile bright" style="left:165px">
  <svg class="icon" width="48" height="48" viewBox="0 0 48 48"><circle cx="24" cy="24" r="20" fill="none" stroke="#111" stroke-width="3"/><circle cx="24" cy="24" r="5" fill="#111"/></svg>
  <span class="num">1</span><span class="label">Revolutionary<br>Concepts</span>
</div>
<div class="tile dark" style="left:385px">
  <svg class="icon" width="40" height="48" viewBox="0 0 40 48"><path d="M4 3h22l10 10v32H4z" fill="none" stroke="#f5e63a" stroke-width="3"/><path d="M11 20h18M11 27h18M11 34h18" stroke="#f5e63a" stroke-width="3"/></svg>
  <span class="num">2</span><span class="label">Detailed<br>Explanations</span>
</div>
<div class="tile bright" style="left:605px">
  <svg class="icon" width="48" height="48" viewBox="0 0 48 48"><circle cx="24" cy="20" r="16" fill="none" stroke="#111" stroke-width="3"/><path d="M18 40h12M20 46h8" stroke="#111" stroke-width="3"/></svg>
  <span class="num">3</span><span class="label">Thought<br>Provoking<br>Examples</span>
</div>
<div class="tile dark" style="left:825px">
  <svg class="icon" width="48" height="48" viewBox="0 0 48 48"><path d="M24 3l6 15h16l-13 10 5 16-14-10-14 10 5-16L2 18h16z" fill="none" stroke="#f5e63a" stroke-width="3" stroke-linejoin="round"/></svg>
  <span class="num">4</span><span class="label">A Touch<br>of Humor</span>
</div>

<p class="tile-copy" style="left:178px">Lorem ipsum dolor sit amet, consectetuer adipiscing elit, sed diam nonummy nibh euismod tincidunt ut laoreet dolore magna aliquam erat volutpat. Ut wisi enim nostrud exerci tation ullamcorper suscipit lobortis nisl</p>
<p class="tile-copy" style="left:393px">Lorem ipsum dolor sit amet, consectetuer adipiscing elit, sed diam nonummy nibh euismod tincidunt ut laoreet dolore magna aliquam erat volutpat. Ut wisi enim nostrud exerci tation ullamcorper suscipit lobortis nisl</p>
<p class="tile-copy" style="left:609px">Lorem ipsum dolor sit amet, consectetuer adipiscing elit, sed diam nonummy nibh euismod tincidunt ut laoreet dolore magna aliquam erat volutpat. Ut wisi enim nostrud exerci tation ullamcorper suscipit lobortis nisl</p>
<p class="tile-copy" style="left:825px">Lorem ipsum dolor sit amet, consectetuer adipiscing elit, sed diam nonummy nibh euismod tincidunt ut laoreet dolore magna aliquam erat volutpat. Ut wisi enim nostrud exerci tation ullamcorper suscipit lobortis nisl</p>

<section class="banner journey">
  <h2 class="headline">Embark on a<br><span class="hl">Mind Bending<br>Journey</span></h2>
  <div class="mockup" role="img" aria-label="Stack of two yellow Quantum Physics books lying at an angle" style="left:378px;top:123px;width:458px;height:380px"></div>
</section>

<section class="banner secrets">
  <h2 class="headline">Discover<br>the Secrets of<br><span class="hl">the Quantum<br>Universe</span></h2>
  <div class="mockup" role="img" aria-label="Yellow Quantum Physics book beside an open copy showing chapter one" style="left:438px;top:50px;width:440px;height:478px;background:linear-gradient(90deg,var(--yellow) 0 12%,#eeeeee 12% 100%)"></div>
</section>

<section class="banner power">
  <h2 class="headline">Unlock<br>the Power<br>of <span class="hl">Quantum<br>Mechanics</span></h2>
  <div class="mockup" role="img" aria-label="Back and front covers of the yellow Quantum Physics book side by side" style="left:404px;top:177px;width:440px;height:355px"></div>
</section>

<hr class="details-rule" style="top:3048px">
<h3 class="details-title">Product details</h3>
<ul class="details">
  <li><b>ASIN</b> : K7Q2FXH58C</li>
  <li><b>Publisher</b> : Independently published (8 Jun. 2024)</li>
  <li><b>Language</b> : English</li>
  <li><b>Paperback</b> : 175 pages</li>
  <li><b>ISBN-13</b> : 979-8000112233</li>
  <li><b>Dimensions</b> : 15.24 x 1.02 x 22.86 cm</li>
  <li><b>Best Sellers Rank:</b> 188,945 in Books (<a href="#">See Top 100 in Books</a>)</li>
  <li><b>Customer reviews:</b> 4.9 <span class="stars">★★★★★</span> ⌄ &nbsp;&nbsp;<a href="#">29 ratings</a></li>
</ul>
<hr class="details-rule" style="top:3316px">

</body>
</html>
```